Header/Banner Design for Website

Looking for a banner/header design for www.fixerupperdiaries.net Should be fun and whimsical, and include the name of the website, something to do with Toolbox Tales or tools, and a caricature of a young, beautiful 20 something blond who the website revolves around. The website is about a young woman who bought her first house and it taking on all of the renovations and remodeling on her own for the first time.

The header/banner should include the same colors that are in the website. The width should be no more than 430 pixels, the height is flexible but the current space in the header is 85 pixels...looking for some creativity. any questions, please ask. Attached an image that she liked for the image of the woman (would like to see versions of this included)
Updates

Target Market(s)

women 20+ that are new home owners or that are tackling Toolbox Tales on their own

Industry/Entity Type

Toolbox Tales

Requirements
Must have
• color coordinate with the website
should feature a young, blond, female caricature
should include the name of the website

```html
<!DOCTYPE html>
<html lang="en">
<head>
<meta charset="utf-8">
<title>Toolbox Tales – Header</title>
<link href="https://fonts.googleapis.com/css2?family=Delius&display=swap" rel="stylesheet">
<style>
  :root {
    --paper: #ffffff;
    --plum: #6d1445;
    --blush: #fde3f0;
    --blush-line: #f6c5de;
  }
  * { margin: 0; padding: 0; box-sizing: border-box; }
  html, body { width: 1200px; height: 237px; overflow: hidden; background: var(--paper); }
  .header {
    position: relative;
    width: 1200px;
    height: 237px;
    background: var(--paper);
  }
  .brand {
    position: absolute;
    left: 14px;
    top: 16px;
    display: flex;
    align-items: center;
    gap: 14px;
  }
  .brand-dot {
    width: 36px;
    height: 36px;
    border-radius: 50%;
    background: var(--plum);
    flex: none;
  }
  .site-name {
    font-family: "Delius", "Comic Sans MS", cursive;
    font-weight: 400;
    font-size: 66px;
    line-height: 1;
    color: var(--plum);
    letter-spacing: 1px;
    white-space: nowrap;
  }
  .band {
    position: absolute;
    left: 0;
    top: 103px;
    width: 1200px;
    height: 25px;
    background: var(--plum);
  }
  .band-edge {
    position: absolute;
    left: 0;
    top: 128px;
    width: 1200px;
    height: 4px;
    background: var(--blush-line);
  }
  .lower {
    position: absolute;
    left: 0;
    top: 132px;
    width: 1200px;
    height: 105px;
    background: var(--blush);
  }
  .mascot {
    position: absolute;
    left: 945px;
    top: 0;
    width: 240px;
    height: 237px;
  }
</style>
</head>
<body>
  <header class="header">
    <div class="lower"></div>
    <div class="band"></div>
    <div class="band-edge"></div>
    <div class="brand">
      <span class="brand-dot"></span>
      <h1 class="site-name">Toolbox Tales</h1>
    </div>
    <svg class="mascot" viewBox="0 0 240 237" role="img" aria-label="Illustration of a cheerful young blond woman in a purple top waving, with small stars">
      <defs>
        <linearGradient id="mascot-tone" x1="0" y1="0" x2="0" y2="1">
          <stop offset="0" stop-color="#f5dc86"/>
          <stop offset="0.45" stop-color="#f3d0b8"/>
          <stop offset="1" stop-color="#c77ad3"/>
        </linearGradient>
      </defs>
      <rect x="0" y="0" width="240" height="237" rx="18" fill="url(#mascot-tone)" opacity="0.9"/>
    </svg>
  </header>
</body>
</html>
```